Modern Business Card For A Digital Advertising Company

I'll be print on the Tarn Prints Velour paper http://us.tarnprints.example/products/velour/business-cards.html
Need's to be modern and use the color palette of the logo or gray scales. I think integrating the pixelation of the logo in to the card and having it wrap from one side to the other could be interesting. My company provides ad operations, web development, and number of other services to websites around the world. You can see my website at http://www.pixelharbor.example
Contact info on the card needs to have
Dana Welloby
President
p.555.318.4406
dana@pixelharbor.example
http://www.pixelharbor.example
Doesn't necessarily need to be in that order
Target Market(s)
Website owners
Industry/Entity Type
Business
Look and feel

```html
<!DOCTYPE html>
<html lang="en">
<head>
<meta charset="utf-8">
<title>Pixel Harbor – Business Card</title>
<link rel="stylesheet" href="https://fonts.googleapis.com/css2?family=Open+Sans:ital,wght@0,600;0,700;1,400&display=swap">
<style>
  :root {
    --page-bg: #e9e9e9;
    --card-black: #000000;
    --text-white: #ffffff;
    --silver-light: #f2f2f2;
    --silver-mid: #c4c4c4;
    --silver-dark: #8a8a8a;
    --brand-green: #8dc63f;
    --green-deep: #0b4a10;
    --green-mid: #3f8a2a;
    --icon-ring: #1a1a1a;
  }
  * { box-sizing: border-box; }
  html, body {
    margin: 0;
    width: 1200px;
    height: 911px;
    overflow: hidden;
    background: var(--page-bg);
    font-family: "Open Sans", Arial, sans-serif;
  }
  .business-card {
    position: absolute;
    left: 67px;
    top: 115px;
    width: 1066px;
    height: 612px;
    background: var(--card-black);
    overflow: hidden;
  }
  .corner-swoosh {
    position: absolute;
    inset: 0;
  }
  .title-band {
    position: absolute;
    left: 0;
    top: 176px;
    width: 178px;
    height: 46px;
    background: linear-gradient(90deg, var(--silver-light), var(--silver-mid) 70%, var(--silver-dark));
    border-radius: 0 23px 23px 0;
  }
  .job-title {
    position: absolute;
    left: 12px;
    top: 180px;
    font-style: italic;
    font-weight: 400;
    font-size: 28px;
    color: #222;
    line-height: 38px;
  }
  .person-name {
    position: absolute;
    left: 178px;
    top: 162px;
    font-weight: 700;
    font-size: 56px;
    letter-spacing: -1px;
    line-height: 72px;
    color: var(--text-white);
  }
  .contact-row {
    position: absolute;
    left: 0;
    height: 52px;
    width: 600px;
  }
  .contact-row .band {
    position: absolute;
    left: 0;
    top: 0;
    width: 192px;
    height: 52px;
    background: linear-gradient(90deg, var(--silver-light), var(--silver-mid) 65%, var(--silver-dark));
    border-radius: 0 26px 26px 0;
  }
  .contact-row .icon {
    position: absolute;
    left: 166px;
    top: -1px;
    width: 54px;
    height: 54px;
  }
  .contact-row .value {
    position: absolute;
    left: 236px;
    top: 0;
    line-height: 52px;
    color: var(--text-white);
    font-weight: 600;
    white-space: nowrap;
  }
  .row-phone { top: 292px; }
  .row-email { top: 354px; }
  .row-web { top: 416px; }
  .row-phone .value { font-size: 44px; font-weight: 700; }
  .row-email .value, .row-web .value { font-size: 25px; }
  .brand-name {
    position: absolute;
    left: 604px;
    top: 292px;
    display: flex;
    align-items: center;
    gap: 16px;
  }
  .brand-mark {
    width: 40px;
    height: 40px;
    background: var(--brand-green);
  }
  .brand-word {
    font-weight: 700;
    font-size: 44px;
    letter-spacing: 2px;
    color: var(--brand-green);
    line-height: 1;
  }
</style>
</head>
<body>
  <section class="business-card">
    <svg class="corner-swoosh" viewBox="0 0 1066 612" width="1066" height="612" aria-hidden="true">
      <defs>
        <linearGradient id="swooshGreen" x1="0" y1="0" x2="1" y2="0">
          <stop offset="0" stop-color="var(--brand-green)"/>
          <stop offset="0.45" stop-color="var(--green-mid)"/>
          <stop offset="1" stop-color="var(--green-deep)"/>
        </linearGradient>
      </defs>
      <path d="M612 0 Q960 70 1066 454 L1066 0 Z" fill="url(#swooshGreen)"/>
      <path d="M700 0 Q990 90 1066 330 L1066 0 Z" fill="var(--green-deep)" opacity="0.35"/>
    </svg>

    <div class="title-band"></div>
    <div class="job-title">President</div>
    <div class="person-name">Dana Welloby</div>

    <div class="contact-row row-phone">
      <div class="band"></div>
      <svg class="icon" viewBox="0 0 54 54" aria-hidden="true">
        <circle cx="27" cy="27" r="25" fill="var(--silver-mid)" stroke="var(--icon-ring)" stroke-width="4"/>
        <rect x="18" y="12" width="18" height="30" rx="3" fill="none" stroke="var(--icon-ring)" stroke-width="2.5"/>
        <rect x="21" y="16" width="12" height="19" fill="var(--icon-ring)"/>
        <circle cx="27" cy="38.5" r="1.6" fill="var(--icon-ring)"/>
      </svg>
      <div class="value">555.318.4406</div>
    </div>

    <div class="contact-row row-email">
      <div class="band"></div>
      <svg class="icon" viewBox="0 0 54 54" aria-hidden="true">
        <circle cx="27" cy="27" r="25" fill="var(--silver-mid)" stroke="var(--icon-ring)" stroke-width="4"/>
        <text x="27" y="37" text-anchor="middle" font-family="Open Sans, Arial, sans-serif" font-size="30" font-weight="600" fill="var(--icon-ring)">@</text>
      </svg>
      <div class="value">dana@pixelharbor.example</div>
    </div>

    <div class="contact-row row-web">
      <div class="band"></div>
      <svg class="icon" viewBox="0 0 54 54" aria-hidden="true">
        <circle cx="27" cy="27" r="25" fill="var(--silver-mid)" stroke="var(--icon-ring)" stroke-width="4"/>
        <circle cx="27" cy="27" r="12" fill="none" stroke="var(--icon-ring)" stroke-width="2.5"/>
        <ellipse cx="27" cy="27" rx="5" ry="12" fill="none" stroke="var(--icon-ring)" stroke-width="2"/>
        <line x1="15" y1="27" x2="39" y2="27" stroke="var(--icon-ring)" stroke-width="2"/>
      </svg>
      <div class="value">www.pixelharbor.example</div>
    </div>

    <div class="brand-name">
      <span class="brand-mark"></span>
      <span class="brand-word">PIXEL HARBOR</span>
    </div>
  </section>
</body>
</html>
```